Banner for construction site to identify developer

we need a 4 foot by 8 foot banner to hang on the fence of a residential townhome development in Phoenix, Arizona that identifies Tolvane Holdings as the company behind the development/project. Also needs to include the logo, phone number, and web address. Would like to stick with the blue colors provided in the attached logo. The blues should stay the same but the letters in the logo can change to another color if necessary. Feel free to use "Tolvane Holdings" in place of "Tolvane Holdings". Looking for use of colors/design to take up space so banner is not just text with a logo.

Target Market(s)

drive by traffic looking at the site

Industry/Entity Type

Real Estate

Colors
0054AA
0677BA
7BADD7
CADEEF
E8F1F8

Requirements
Must have
• company name, phone number and web address

```html
<!DOCTYPE html>
<html lang="en">
<head>
<meta charset="utf-8">
<title>Tolvane Holdings – Site Banner</title>
<link href="https://fonts.googleapis.com/css2?family=Bebas+Neue&family=Montserrat:wght@600;700;900&family=Comfortaa:wght@700&display=swap" rel="stylesheet">
<style>
  :root {
    --backdrop: #b3b3b3;
    --paper: #ffffff;
    --brand-deep: #1e6fa1;
    --brand-bright: #1aa7dc;
    --ink: #333a40;
    --accent: #f5c631;
    --accent-ink: #0f2a44;
  }
  * { margin: 0; padding: 0; box-sizing: border-box; }
  html, body {
    width: 954px; height: 1200px; overflow: hidden;
    background: var(--backdrop);
  }
  .banner {
    position: absolute; left: 177px; top: 0;
    width: 600px; height: 1200px;
    background: var(--paper);
    overflow: hidden;
  }
  .banner__shapes { position: absolute; inset: 0; }
  .brand {
    position: absolute; top: 92px; left: 0; width: 100%;
    display: flex; justify-content: center; align-items: center; gap: 12px;
  }
  .brand__mark {
    width: 34px; height: 34px; background: var(--brand-bright);
  }
  .brand__name {
    font-family: "Montserrat", sans-serif; font-weight: 700;
    font-size: 38px; color: var(--ink); letter-spacing: -0.5px;
  }
  .hero-visual {
    position: absolute; left: 76px; top: 204px; width: 448px; height: 380px;
    background: linear-gradient(180deg, #dbe6ee 0%, #c9d4dc 35%, #d9b894 70%, #3b4650 100%);
    clip-path: polygon(8% 10%, 92% 8%, 100% 40%, 98% 85%, 62% 100%, 2% 82%, 0 40%);
    opacity: .9;
  }
  .headline {
    position: absolute; left: 0; width: 100%; text-align: center; color: var(--paper);
  }
  .headline__lead {
    top: 716px; font-family: "Bebas Neue", sans-serif; font-weight: 400;
    font-size: 96px; line-height: 1; letter-spacing: 1px;
  }
  .headline__main {
    top: 800px; font-family: "Montserrat", sans-serif; font-weight: 900;
    font-size: 128px; line-height: 1; letter-spacing: -2px;
  }
  .headline__tail {
    top: 928px; font-family: "Comfortaa", sans-serif; font-weight: 700;
    font-size: 84px; line-height: 1;
  }
  .web-pill {
    position: absolute; left: 144px; top: 1033px; width: 312px; height: 54px;
    border-radius: 27px; background: var(--accent);
    display: flex; align-items: center; justify-content: center;
    font-family: "Montserrat", sans-serif; font-weight: 700; font-size: 19px;
    color: var(--accent-ink);
  }
  .contact-line {
    position: absolute; left: 0; top: 1106px; width: 100%; text-align: center;
    font-family: "Bebas Neue", sans-serif; font-size: 36px; color: var(--paper);
    letter-spacing: 0.5px;
  }
</style>
</head>
<body>
  <main class="banner">
    <svg class="banner__shapes" width="600" height="1200" viewBox="0 0 600 1200" aria-hidden="true">
      <defs>
        <linearGradient id="bandFade" x1="0" x2="1" y1="0" y2="0">
          <stop offset="0" stop-color="#1aa7dc" stop-opacity="0"/>
          <stop offset="0.15" stop-color="#1aa7dc"/>
          <stop offset="0.85" stop-color="#1aa7dc"/>
          <stop offset="1" stop-color="#1aa7dc" stop-opacity="0"/>
        </linearGradient>
      </defs>
      <polygon class="panel-blue" fill="var(--brand-deep)" points="0,533 339,584 600,519 600,1200 0,1200"/>
      <polygon class="chevron-band" fill="url(#bandFade)" points="15,562 339,587 585,551 585,575 339,609 15,587"/>
      <polygon class="chevron-band" fill="url(#bandFade)" points="15,616 339,648 585,612 585,640 339,670 15,645"/>
      <polygon class="chevron-band chevron-band--faint" fill="url(#bandFade)" opacity="0.35" points="15,645 339,670 585,640 585,660 339,703 15,662"/>
    </svg>

    <header class="brand">
      <span class="brand__mark"></span>
      <span class="brand__name">Tolvane Holdings</span>
    </header>

    <div class="hero-visual" role="img" aria-label="Illustration of a modern multi-storey glass home with rooftop gardens and lit interiors"></div>

    <h1>
      <span class="headline headline__lead">Looking for a</span>
      <span class="headline headline__main">DREAM</span>
      <span class="headline headline__tail">HOME</span>
    </h1>

    <div class="web-pill">www.tolvaneholdings.com</div>
    <p class="contact-line">For more info : 05550 18247</p>
  </main>
</body>
</html>
```